Postcard Design

I run a kitchen cabinet company that sells pre-manufactured cabinets, specially made by Brindlewood Cabinets. You can see their website at brindlewoodcabinets-example.com and my website at thelarchbenchco-example.com. In addition to selling cabinets I sell counter tops (laminate and granite) along with appliances.

I need a postcard design that will be targeted at new home owners who recently purchased their property and may need kitchen cabinets, counter tops and/or appliances. I do not need a list of new home owners, I will have that.

My 'shtick' is I offer FREE Delivery and FREE Installation.
When I talk to customers about pricing I routinely come in 20-30% cheaper than the big box stores.

New Home Owners - not new construction

It Company

```html
<!DOCTYPE html>
<html lang="en">
<head>
<meta charset="utf-8">
<title>The Larch Bench Co Postcard</title>
<link href="https://fonts.googleapis.com/css2?family=Montserrat:wght@700&family=Arimo:ital,wght@0,400;0,700;1,700&display=swap" rel="stylesheet">
<style>
  :root {
    --wood-dark: #2e0f0f;
    --wood-mid: #47191a;
    --stripe-green: #1c7a45;
    --accent-orange: #f0a46e;
    --footer-orange: #d8672a;
    --ink-white: #ffffff;
    --ink-black: #111111;
  }
  html, body { margin: 0; padding: 0; overflow: hidden; }
  body { width: 1200px; height: 929px; background: #ffffff; }
  .postcard {
    position: relative; width: 1200px; height: 929px; overflow: hidden;
    font-family: "Arimo", Arial, sans-serif;
    background: linear-gradient(100deg, var(--wood-dark) 0%, var(--wood-mid) 35%, var(--wood-dark) 60%, var(--wood-mid) 100%);
  }
  .stripe { position: absolute; left: 0; width: 1200px; height: 36px; background: var(--stripe-green); }
  .stripe-top { top: 54px; }
  .stripe-bottom { top: 198px; }
  .brand-name {
    position: absolute; top: 118px; left: 0; width: 1200px; margin: 0;
    text-align: center; font-family: "Montserrat", Arial, sans-serif; font-weight: 700;
    font-size: 58px; line-height: 64px; letter-spacing: -1px; color: var(--ink-white);
  }
  .offer-box {
    position: absolute; left: 99px; top: 264px; width: 508px; height: 165px;
    border: 4px solid var(--ink-white); box-sizing: border-box;
    padding: 10px 0 0 14px; color: var(--ink-white);
  }
  .offer-line { margin: 0; font-size: 56px; line-height: 70px; white-space: nowrap; }
  .offer-line strong { font-style: italic; font-weight: 700; }
  .service { position: absolute; margin: 0; font-size: 40px; line-height: 46px; color: var(--accent-orange); white-space: nowrap; }
  .service-cabinets { left: 114px; top: 457px; }
  .service-countertops { left: 114px; top: 550px; }
  .service-installation { left: 426px; top: 550px; }
  .service-appliances { left: 114px; top: 646px; }
  .kitchen-photo {
    position: absolute; left: 666px; top: 264px; width: 459px; height: 462px;
    background: linear-gradient(160deg, #e08a3c 0%, #c46f2e 30%, #3a2420 55%, #1e1412 100%);
  }
  .tagline {
    position: absolute; left: 753px; top: 606px; margin: 0;
    font-size: 42px; line-height: 48px; font-weight: 700; color: var(--ink-white);
  }
  .contact-band {
    position: absolute; left: 0; top: 729px; width: 1200px; height: 200px;
    background: var(--footer-orange);
  }
  .contact-item {
    position: absolute; top: 806px; height: 50px; display: flex; align-items: center; gap: 22px;
    font-size: 36px; line-height: 50px; color: var(--ink-black); white-space: nowrap;
  }
  .contact-phone { left: 160px; }
  .contact-email { left: 640px; }
  .contact-item svg { display: block; flex: none; }
</style>
</head>
<body>
<div class="postcard">
  <div class="stripe stripe-top"></div>
  <div class="stripe stripe-bottom"></div>
  <h1 class="brand-name">THE LARCH BENCH CO</h1>

  <div class="offer-box">
    <p class="offer-line"><strong>FREE</strong> Delivery!</p>
    <p class="offer-line"><strong>FREE</strong> Instalation!</p>
  </div>

  <p class="service service-cabinets">Cabinets</p>
  <p class="service service-countertops">Countertops</p>
  <p class="service service-installation">Instalation</p>
  <p class="service service-appliances">Appliances</p>

  <div class="kitchen-photo" role="img" aria-label="Photo of a finished kitchen with dark espresso cabinets against warm orange walls"></div>
  <p class="tagline">Dependable<br>Workmanship!</p>

  <div class="contact-band"></div>
  <div class="contact-item contact-phone">
    <svg width="50" height="50" viewBox="0 0 24 24" aria-hidden="true">
      <path fill="#111" d="M6.6 10.8a15.1 15.1 0 0 0 6.6 6.6l2.2-2.2c.3-.3.7-.4 1-.2 1.1.4 2.3.6 3.6.6.6 0 1 .4 1 1V20c0 .6-.4 1-1 1A17 17 0 0 1 3 4c0-.6.4-1 1-1h3.5c.6 0 1 .4 1 1 0 1.3.2 2.5.6 3.6.1.3 0 .7-.2 1z"/>
    </svg>
    <span>(000)000-0000</span>
  </div>
  <div class="contact-item contact-email">
    <svg width="58" height="42" viewBox="0 0 58 42" aria-hidden="true">
      <rect x="0" y="0" width="58" height="42" rx="3" fill="#111"/>
      <path d="M3 4 L29 24 L55 4" fill="none" stroke="#d8672a" stroke-width="3"/>
    </svg>
    <span>hi@larchbench-ex.com</span>
  </div>
</div>
</body>
</html>
```